Web Calculator design Housing Investment

We have a web calculator that needs to be fixed from a design perspective. The key tasks are:<br/>1. Selecting icons / pictures / colours for the various steps<br/>2. Designing navigation between calculator steps<br/>3. Making suggestions for chart design. The limitation is that the charts are all using the Tarvo API (the same charts that Tarvo Grids use).<br/><br/>There are four entry screens and then a result screen. See attached PDF for screenshots. You can see our website at https://brindlecapital.com for our corporate colours and style.

Target Market(s)

Real Estate Investors

Industry/Entity Type

Financial Planning

Number of Pages Required

1 page

Font styles to use
Sans Serif
Other font styles liked:
• Ubuntu

Colors
86cae7
3176b5
0455a3
ffffff

Requirements
Must have
• New Icons
• Suggested design for navigation
• Suggested design for charts

```html
<!DOCTYPE html>
<html lang="en">
<head>
<meta charset="utf-8">
<title>Property Investment Calculator – Screen Designs</title>
<link href="https://fonts.googleapis.com/css2?family=IBM+Plex+Sans:wght@400;500;600;700&display=swap" rel="stylesheet">
<style>
:root{
  --canvas:#8c8c8c;
  --navy:#0455a3;
  --step:#1c4da1;
  --brand:#3176b5;
  --sky:#86cae7;
  --ink:#2b2b2b;
  --muted:#666;
  --page:#f4f1f4;
  --white:#ffffff;
  --grey-btn:#9b9b9b;
  --foot:#6b6b6b;
  --foot-legal:#5c5c5c;
  --line:#d9d9d9;
  --teal:#2ec4c8;
  --teal-soft:#e3f4f6;
}
*{box-sizing:border-box;margin:0;padding:0}
html,body{width:683px;height:1200px;overflow:hidden}
body{background:var(--canvas);font-family:"IBM Plex Sans",Arial,sans-serif;color:var(--ink);position:relative}

.screen{position:absolute;width:658px;transform-origin:0 0;transform:scale(.469);display:flex;flex-direction:column;background:var(--page)}
.screen.s1{left:21.6px;top:21px;height:733px}
.screen.s2{left:354.6px;top:21px;height:733px}
.screen.s3{left:21.6px;top:384.6px;height:733px}
.screen.s4{left:354.6px;top:384.6px;height:927px}
.screen.s5{left:21.6px;top:752.4px;height:927px}

/* header */
.site-head{height:55px;background:var(--white);position:relative;flex:none}
.brand{position:absolute;left:72px;top:17px;font-size:14px;font-weight:600;color:#1d2a5a;display:flex;align-items:center;gap:5px}
.brand .dot{width:8px;height:8px;border-radius:50%;background:var(--navy)}
.main-nav{position:absolute;left:436px;top:23px;display:flex;gap:8px;font-size:5.5px;font-weight:600;color:#555}
.main-nav .current{color:var(--navy);border-bottom:1.5px solid var(--navy);padding-bottom:3px}
.main-nav .search{width:6px;height:6px;border:1px solid #555;border-radius:50%}

/* body */
.page{flex:1;position:relative}
.card{position:absolute;left:72px;top:42px;width:515px;background:var(--white);box-shadow:0 6px 10px rgba(0,0,0,.08)}
.s1 .card,.s2 .card{height:301px}
.s3 .card{height:303px}
.s4 .card,.s5 .card{height:486px}

.steps{position:absolute;left:0;top:0;width:100%;height:50px}
.step{position:absolute;top:-9px;width:110px;margin-left:-55px;text-align:center}
.step:nth-child(1){left:46px}.step:nth-child(2){left:144px}.step:nth-child(3){left:250px}.step:nth-child(4){left:370px}.step:nth-child(5){left:473px}
.step .num{display:block;margin:0 auto;width:18px;height:18px;border-radius:50%;background:var(--white);color:#333;font-size:9px;line-height:18px}
.step .ico{display:block;margin:8px auto 5px;width:13px;height:13px;color:#555}
.step .lbl{font-size:6.5px;color:#333}
.step.on .num{background:var(--step);color:var(--white)}
.step.on .ico{color:var(--brand)}
.step.on .lbl{color:var(--navy);font-weight:700}

.question{position:absolute;left:0;width:100%;text-align:center;font-size:13px;color:#333}
.btns{position:absolute;left:200px;display:flex;gap:11px}
.btn{height:18px;padding:0 9px;min-width:52px;font-size:7px;font-weight:600;color:var(--white);display:flex;align-items:center;justify-content:center;letter-spacing:.3px}
.btn.prev{background:var(--grey-btn)}
.btn.next{background:var(--sky)}

/* screen 1 tiles */
.type-tile{position:absolute;top:128px;width:96px;height:96px;border:1px solid #d9c9d3;display:flex;flex-direction:column;align-items:center;justify-content:center;gap:10px;font-size:9px;font-weight:700;color:var(--navy)}
.type-tile svg{width:38px;height:38px}
.type-tile.unit{left:154px;background:var(--navy);color:var(--white);border-color:var(--navy)}
.type-tile.house{left:264px}

/* sliders */
.field-label{position:absolute;font-size:9px;color:#333}
.slider{position:absolute;height:2px;background:var(--line)}
.slider .fill{position:absolute;left:0;top:-0.5px;height:3px;background:var(--navy)}
.slider .knob{position:absolute;top:-3.5px;width:9px;height:9px;margin-left:-4.5px;border-radius:50%;background:var(--navy)}
.slider-value{position:absolute;font-size:7px;color:#333}
.map-area{position:absolute;left:328px;top:95px;width:167px;height:155px;background:linear-gradient(135deg,#5a5a5a,#8e8e8e 60%,#6d6d6d);border-radius:40% 45% 35% 50%}

/* screen 3 options */
.method{position:absolute;top:119px;width:147px;height:125px;border:1px solid #bdbdbd;text-align:center;padding-top:14px}
.method svg{width:36px;height:32px;color:#444}
.method h3{font-size:9px;font-weight:600;margin:8px 0 6px;color:#333}
.method p{font-size:6.5px;line-height:9px;color:#555;padding:0 18px}

/* selects */
.select{position:absolute;height:22px;border:1px solid #8f8f8f;background:var(--white);font-size:7px;padding:0 8px;display:flex;align-items:center;justify-content:space-between;color:#333}
.select::after{content:"";border:3px solid transparent;border-top:3.5px solid #333;margin-top:3px}
.note{position:absolute;font-size:7px;line-height:9px;color:#333}
.chart{position:absolute;left:0;top:0;overflow:visible}
.chart text{font-family:"IBM Plex Sans",Arial,sans-serif;font-size:7px;fill:#555}

/* screen 5 */
.calc-form{position:absolute;left:15px;top:76px;width:485px;height:119px;border:1px solid #cfcfcf}
.cap{position:absolute;font-size:7px;font-weight:700;color:#333}
.results{position:absolute;left:18px;top:360px;width:482px;height:52px;background:#f0f0f0}
.result{position:absolute;font-size:7px;color:#333}
.result b{display:block;font-weight:700;margin-bottom:3px}

/* footer */
.site-foot{flex:none;height:294px;display:flex;flex-direction:column}
.foot-main{height:227px;background:var(--foot);position:relative;color:#f2f2f2}
.foot-col{position:absolute;top:18px}
.foot-col h4{font-size:6.5px;font-weight:700;letter-spacing:.2px;margin-bottom:12px}
.foot-col p{font-size:5.8px;line-height:10.8px;margin-bottom:8px}
.about{left:94px;width:150px}
.news{left:252px;width:140px}
.news li{list-style:none;font-size:5.8px;line-height:7.6px;padding:3px 7px;border-bottom:1px solid #777;margin-bottom:4px}
.social{display:flex;gap:3px;margin-top:-2px}
.social i{width:9px;height:9px;border-radius:50%;border:1px solid #eee}
.badge{display:block;width:38px;height:6px;background:#f4f4f4;margin-top:5px;border-radius:1px}
.register{left:410px;width:145px}
.reg-box{background:#f3f3f3;height:167px;padding:16px 20px;text-align:center}
.reg-box p{font-size:6px;font-weight:600;line-height:10px;color:#333;margin-bottom:6px}
.reg-box span{display:block;background:var(--brand);color:var(--white);font-size:5.8px;line-height:10px;padding:3px 4px;margin-bottom:6px}
.foot-legal{flex:1;background:var(--foot-legal);padding:9px 94px 0;color:#c9c9c9;font-size:5.2px;line-height:10px}
.foot-legal .links{color:#aaa;font-size:4.6px;margin-top:3px}
</style>
</head>
<body>

<svg width="0" height="0" style="position:absolute" aria-hidden="true">
  <defs>
    <symbol id="i-unit" viewBox="0 0 16 16"><g fill="none" stroke="currentColor" stroke-width="1.2"><rect x="3" y="2" width="10" height="12"/><path d="M5 5h2M9 5h2M5 8h2M9 8h2M7 14v-3h2v3"/></g></symbol>
    <symbol id="i-pin" viewBox="0 0 16 16"><g fill="none" stroke="currentColor" stroke-width="1.2"><path d="M8 15s5-5 5-8.5a5 5 0 0 0-10 0C3 10 8 15 8 15z"/><circle cx="8" cy="6.5" r="1.8"/></g></symbol>
    <symbol id="i-value" viewBox="0 0 16 16"><g fill="none" stroke="currentColor" stroke-width="1.2"><circle cx="8" cy="8" r="6"/><path d="M10 5.5H7a1.3 1.3 0 0 0 0 2.6h2a1.3 1.3 0 0 1 0 2.6H6M8 4v8"/></g></symbol>
    <symbol id="i-forecast" viewBox="0 0 16 16"><g fill="none" stroke="currentColor" stroke-width="1.2"><rect x="2" y="2" width="12" height="12" rx="1"/><path d="M4 11l3-3 2 2 3-4"/></g></symbol>
    <symbol id="i-calc" viewBox="0 0 16 16"><g fill="none" stroke="currentColor" stroke-width="1.2"><rect x="3.5" y="1.5" width="9" height="13" rx="1"/><path d="M5.5 4h5M5.5 7.5h1M8 7.5h1M10 7.5h.5M5.5 10h1M8 10h1M10 10h.5M5.5 12.5h1M8 12.5h1"/></g></symbol>
  </defs>
</svg>

<!-- Step 1: property type -->
<section class="screen s1">
  <header class="site-head"><div class="brand"><span class="dot"></span>Brindle Capital</div><nav class="main-nav"><span class="current">INVEST WITH US ⌄</span><span>CONTENT ⌄</span><span>CLIENT LOGIN</span><span class="search"></span></nav></header>
  <main class="page">
    <div class="card">
      <div class="steps">
        <div class="step on"><span class="num">1</span><svg class="ico"><use href="#i-unit"/></svg><span class="lbl">PROPERTY TYPE</span></div>
        <div class="step"><span class="num">2</span><svg class="ico"><use href="#i-pin"/></svg><span class="lbl">PROPERTY LOCATION</span></div>
        <div class="step"><span class="num">3</span><svg class="ico"><use href="#i-value"/></svg><span class="lbl">PROPERTY VALUATION</span></div>
        <div class="step"><span class="num">4</span><svg class="ico"><use href="#i-forecast"/></svg><span class="lbl">YOUR PROPERTY FORECAST</span></div>
        <div class="step"><span class="num">5</span><svg class="ico"><use href="#i-calc"/></svg><span class="lbl">CALCULATION</span></div>
      </div>
      <p class="question" style="top:86px">What type of Property would like to compare?</p>
      <div class="type-tile unit"><svg viewBox="0 0 40 40" fill="none" stroke="currentColor" stroke-width="2"><path d="M10 6h20M8 10h24v26H8z"/><path d="M13 15h4v4h-4zM23 15h4v4h-4zM13 23h4v4h-4zM23 23h4v4h-4zM17 36v-6h6v6"/></svg>UNIT</div>
      <div class="type-tile house"><svg viewBox="0 0 40 40" fill="none" stroke="currentColor" stroke-width="2"><path d="M4 20L20 8l16 12"/><path d="M8 17v17h24V17"/><rect x="12" y="23" width="5" height="5" fill="currentColor"/><rect x="22" y="23" width="5" height="11"/></svg>HOUSE</div>
      <div class="btns" style="top:256px"><span class="btn prev">PREVIOUS</span><span class="btn next">NEXT</span></div>
    </div>
  </main>
  <footer class="site-foot">
    <div class="foot-main">
      <div class="foot-col about"><h4>ABOUT US</h4><p>Brindle Capital was formed to bridge the gap in investment solutions for everyday people looking for the middle ground between cookie-cutter robo-advice and high-cost financial planning.</p><p>Brindle Capital products put the power back in your hands:<br>⇒ tax efficient structures,<br>⇒ tailored to your ethics,<br>⇒ tailored to your risk,<br>⇒ tailored to your income needs,<br>⇒ fully transparent.</p><div class="social"><i></i><i></i><i></i><i></i><i></i><i></i><i></i></div><span class="badge"></span></div>
      <div class="foot-col news"><h4>LATEST NEWS</h4><ul><li>Effective Ethical Investment with Owen Marsh | Brindle Investment Insights Podcast</li><li>GDP Hotspots</li><li>Brindle Capital featured on Ledger Point Analytics' Webinar with Alan Reeve</li><li>Private sector capex: Not riding to the rescue</li></ul></div>
      <div class="foot-col register"><h4>REGISTER</h4><div class="reg-box"><p>Interested in investing with Brindle Capital?</p><span>Yes - I am ready to get started</span><span>Yes - I'm not ready to invest, but keep me updated on developments</span></div></div>
    </div>
    <div class="foot-legal"><p>The information on this site contains general information and does not take into account your personal objectives, financial situation or needs. Past performance is not an indication of future performance. Brindle Capital Management (ABN 12 345 678 901) is a Corporate Authorised Representative of Brindle Advice Pty Ltd - AFSL 402117. Click here for our Financial Services Guide.</p><p class="links">INVEST WITH US &nbsp; BLOG &nbsp; CLIENT LOGIN</p><p>Copyright 2019 © Brindle Capital</p></div>
  </footer>
</section>

<!-- Step 2: property location -->
<section class="screen s2">
  <header class="site-head"><div class="brand"><span class="dot"></span>Brindle Capital</div><nav class="main-nav"><span class="current">INVEST WITH US ⌄</span><span>CONTENT ⌄</span><span>CLIENT LOGIN</span><span class="search"></span></nav></header>
  <main class="page">
    <div class="card">
      <div class="steps">
        <div class="step on"><span class="num">1</span><svg class="ico"><use href="#i-unit"/></svg><span class="lbl">PROPERTY TYPE</span></div>
        <div class="step on"><span class="num">2</span><svg class="ico"><use href="#i-pin"/></svg><span class="lbl">PROPERTY LOCATION</span></div>
        <div class="step"><span class="num">3</span><svg class="ico"><use href="#i-value"/></svg><span class="lbl">PROPERTY VALUATION</span></div>
        <div class="step"><span class="num">4</span><svg class="ico"><use href="#i-forecast"/></svg><span class="lbl">YOUR PROPERTY FORECAST</span></div>
        <div class="step"><span class="num">5</span><svg class="ico"><use href="#i-calc"/></svg><span class="lbl">CALCULATION</span></div>
      </div>
      <p class="question" style="top:86px;left:27px;text-align:left">Where would this property be located?</p>
      <span class="field-label" style="left:27px;top:130px">How much will the property cost?</span>
      <div class="slider" style="left:28px;top:156px;width:226px"><span class="fill" style="width:90px"></span><span class="knob" style="left:90px"></span></div>
      <span class="slider-value" style="left:258px;top:152px">$500,000</span>
      <span class="field-label" style="left:27px;top:188px">How much will you invest?</span>
      <div class="slider" style="left:28px;top:213px;width:226px"><span class="fill" style="width:64px"></span><span class="knob" style="left:64px"></span></div>
      <span class="slider-value" style="left:258px;top:209px">$200,000</span>
      <div class="map-area" role="img" aria-label="Map of Australia with states shaded in greys for selecting a location"></div>
      <div class="btns" style="top:256px"><span class="btn prev">PREVIOUS</span><span class="btn next">NEXT</span></div>
    </div>
  </main>
  <footer class="site-foot">
    <div class="foot-main">
      <div class="foot-col about"><h4>ABOUT US</h4><p>Brindle Capital was formed to bridge the gap in investment solutions for everyday people looking for the middle ground between cookie-cutter robo-advice and high-cost financial planning.</p><p>Brindle Capital products put the power back in your hands:<br>⇒ tax efficient structures,<br>⇒ tailored to your ethics,<br>⇒ tailored to your risk,<br>⇒ tailored to your income needs,<br>⇒ fully transparent.</p><div class="social"><i></i><i></i><i></i><i></i><i></i><i></i><i></i></div><span class="badge"></span></div>
      <div class="foot-col news"><h4>LATEST NEWS</h4><ul><li>Effective Ethical Investment with Owen Marsh | Brindle Investment Insights Podcast</li><li>GDP Hotspots</li><li>Brindle Capital featured on Ledger Point Analytics' Webinar with Alan Reeve</li><li>Private sector capex: Not riding to the rescue</li></ul></div>
      <div class="foot-col register"><h4>REGISTER</h4><div class="reg-box"><p>Interested in investing with Brindle Capital?</p><span>Yes - I am ready to get started</span><span>Yes - I'm not ready to invest, but keep me updated on developments</span></div></div>
    </div>
    <div class="foot-legal"><p>The information on this site contains general information and does not take into account your personal objectives, financial situation or needs. Past performance is not an indication of future performance. Brindle Capital Management (ABN 12 345 678 901) is a Corporate Authorised Representative of Brindle Advice Pty Ltd - AFSL 402117. Click here for our Financial Services Guide.</p><p class="links">INVEST WITH US &nbsp; BLOG &nbsp; CLIENT LOGIN</p><p>Copyright 2019 © Brindle Capital</p></div>
  </footer>
</section>

<!-- Step 3: valuation method -->
<section class="screen s3">
  <header class="site-head"><div class="brand"><span class="dot"></span>Brindle Capital</div><nav class="main-nav"><span class="current">INVEST WITH US ⌄</span><span>CONTENT ⌄</span><span>CLIENT LOGIN</span><span class="search"></span></nav></header>
  <main class="page">
    <div class="card">
      <div class="steps">
        <div class="step on"><span class="num">1</span><svg class="ico"><use href="#i-unit"/></svg><span class="lbl">PROPERTY TYPE</span></div>
        <div class="step on"><span class="num">2</span><svg class="ico"><use href="#i-pin"/></svg><span class="lbl">PROPERTY LOCATION</span></div>
        <div class="step on"><span class="num">3</span><svg class="ico"><use href="#i-value"/></svg><span class="lbl">PROPERTY VALUATION</span></div>
        <div class="step"><span class="num">4</span><svg class="ico"><use href="#i-forecast"/></svg><span class="lbl">YOUR PROPERTY FORECAST</span></div>
        <div class="step"><span class="num">5</span><svg class="ico"><use href="#i-calc"/></svg><span class="lbl">CALCULATION</span></div>
      </div>
      <p class="question" style="top:77px">How would you like to forecast the returns from property?</p>
      <div class="method" style="left:22px"><svg viewBox="0 0 36 32" fill="none" stroke="currentColor" stroke-width="1.5"><circle cx="20" cy="9" r="7"/><path d="M22 6h-3a1.5 1.5 0 0 0 0 3h2a1.5 1.5 0 0 1 0 3h-3"/><path d="M4 24l6-5h8l-2 4h-5M4 28l4-2h14l8-8"/></svg><h3>Relative cost</h3><p>Use this to value property based on mortgage cost relative to rent cost</p></div>
      <div class="method" style="left:184px"><svg viewBox="0 0 36 32" fill="none" stroke="currentColor" stroke-width="1.5"><rect x="10" y="3" width="16" height="16"/><circle cx="18" cy="11" r="4"/><path d="M6 21h24M6 25h24M6 29h24"/></svg><h3>Relative to Wages</h3><p>Use this to value property based on mortgage cost relative to Relative to Wages</p></div>
      <div class="method" style="left:349px"><svg viewBox="0 0 36 32" fill="none" stroke="currentColor" stroke-width="3"><circle cx="11" cy="8" r="5"/><circle cx="25" cy="24" r="5"/><path d="M28 3L8 29"/></svg><h3>Using Rental Yield</h3><p>Use this to value property based on a rental yield</p></div>
      <div class="btns" style="top:263px"><span class="btn prev">PREVIOUS</span><span class="btn next">NEXT</span></div>
    </div>
  </main>
  <footer class="site-foot">
    <div class="foot-main">
      <div class="foot-col about"><h4>ABOUT US</h4><p>Brindle Capital was formed to bridge the gap in investment solutions for everyday people looking for the middle ground between cookie-cutter robo-advice and high-cost financial planning.</p><p>Brindle Capital products put the power back in your hands:<br>⇒ tax efficient structures,<br>⇒ tailored to your ethics,<br>⇒ tailored to your risk,<br>⇒ tailored to your income needs,<br>⇒ fully transparent.</p><div class="social"><i></i><i></i><i></i><i></i><i></i><i></i><i></i></div><span class="badge"></span></div>
      <div class="foot-col news"><h4>LATEST NEWS</h4><ul><li>Effective Ethical Investment with Owen Marsh | Brindle Investment Insights Podcast</li><li>GDP Hotspots</li><li>Brindle Capital featured on Ledger Point Analytics' Webinar with Alan Reeve</li><li>Private sector capex: Not riding to the rescue</li></ul></div>
      <div class="foot-col register"><h4>REGISTER</h4><div class="reg-box"><p>Interested in investing with Brindle Capital?</p><span>Yes - I am ready to get started</span><span>Yes - I'm not ready to invest, but keep me updated on developments</span></div></div>
    </div>
    <div class="foot-legal"><p>The information on this site contains general information and does not take into account your personal objectives, financial situation or needs. Past performance is not an indication of future performance. Brindle Capital Management (ABN 12 345 678 901) is a Corporate Authorised Representative of Brindle Advice Pty Ltd - AFSL 402117. Click here for our Financial Services Guide.</p><p class="links">INVEST WITH US &nbsp; BLOG &nbsp; CLIENT LOGIN</p><p>Copyright 2019 © Brindle Capital</p></div>
  </footer>
</section>

<!-- Step 4: forecast -->
<section class="screen s4">
  <header class="site-head"><div class="brand"><span class="dot"></span>Brindle Capital</div><nav class="main-nav"><span class="current">INVEST WITH US ⌄</span><span>CONTENT ⌄</span><span>CLIENT LOGIN</span><span class="search"></span></nav></header>
  <main class="page">
    <div class="card">
      <div class="steps">
        <div class="step on"><span class="num">1</span><svg class="ico"><use href="#i-unit"/></svg><span class="lbl">PROPERTY TYPE</span></div>
        <div class="step on"><span class="num">2</span><svg class="ico"><use href="#i-pin"/></svg><span class="lbl">PROPERTY LOCATION</span></div>
        <div class="step on"><span class="num">3</span><svg class="ico"><use href="#i-value"/></svg><span class="lbl">PROPERTY VALUATION</span></div>
        <div class="step on"><span class="num">4</span><svg class="ico"><use href="#i-forecast"/></svg><span class="lbl">YOUR PROPERTY FORECAST</span></div>
        <div class="step"><span class="num">5</span><svg class="ico"><use href="#i-calc"/></svg><span class="lbl">CALCULATION</span></div>
      </div>
      <p class="question" style="top:76px">Your Property Price Forecast</p>
      <p class="note" style="left:69px;top:119px">You have chosen to forecast<br>property prices using</p>
      <p class="note" style="left:276px;top:119px">You can see how this ration has changes over time<br>(in blue) below vs your assumption (in red) for</p>
      <div class="select" style="left:69px;top:149px;width:160px">Gross Rental Yield</div>
      <div class="select" style="left:277px;top:149px;width:160px">Gross Rental Yield</div>
      <svg class="chart" width="515" height="486" viewBox="0 0 515 486" aria-label="Line chart of gross rental yield over time">
        <g stroke="#d6e3f2" stroke-width="1">
          <path d="M110 208H392M110 233H392M110 258H392M110 284H392M110 309H392"/>
        </g>
        <path d="M110 208V335H392" fill="none" stroke="#333" stroke-width="1"/>
        <g text-anchor="end"><text x="102" y="211">1000</text><text x="102" y="236">700</text><text x="102" y="261">500</text><text x="102" y="287">300</text><text x="102" y="312">100</text><text x="102" y="338">0</text></g>
        <g text-anchor="middle"><text x="121" y="353">100</text><text x="148" y="353">200</text><text x="174" y="353">300</text><text x="200" y="353">400</text><text x="226" y="353">500</text><text x="252" y="353">600</text><text x="278" y="353">600</text><text x="304" y="353">700</text><text x="330" y="353">800</text><text x="356" y="353">900</text><text x="382" y="353">1000</text></g>
        <polyline points="121,307 144,323 172,283 197,308 225,283 275,283 302,231 329,309 353,309 391,210" fill="none" stroke="#1a3fe0" stroke-width="1.8"/>
        <g fill="#1a3fe0"><circle cx="121" cy="307" r="2.2"/><circle cx="144" cy="323" r="2.2"/><circle cx="172" cy="283" r="2.2"/><circle cx="197" cy="308" r="2.2"/><circle cx="225" cy="283" r="2.2"/><circle cx="275" cy="283" r="2.2"/><circle cx="302" cy="231" r="2.2"/><circle cx="329" cy="309" r="2.2"/><circle cx="353" cy="309" r="2.2"/><circle cx="391" cy="210" r="2.2"/></g>
      </svg>
      <p class="note" style="left:0;width:100%;text-align:center;top:385px">By default we assume the ratio stays at the latest value of 3.4%. You can change this assumption using the slider</p>
      <div class="slider" style="left:72px;top:411px;width:354px"><span class="fill" style="width:89px"></span><span class="knob" style="left:89px"></span></div>
      <span class="slider-value" style="left:434px;top:407px">3.4%</span>
      <div class="btns" style="top:440px"><span class="btn prev">PREVIOUS</span><span class="btn next">NEXT</span></div>
    </div>
  </main>
  <footer class="site-foot">
    <div class="foot-main">
      <div class="foot-col about"><h4>ABOUT US</h4><p>Brindle Capital was formed to bridge the gap in investment solutions for everyday people looking for the middle ground between cookie-cutter robo-advice and high-cost financial planning.</p><p>Brindle Capital products put the power back in your hands:<br>⇒ tax efficient structures,<br>⇒ tailored to your ethics,<br>⇒ tailored to your risk,<br>⇒ tailored to your income needs,<br>⇒ fully transparent.</p><div class="social"><i></i><i></i><i></i><i></i><i></i><i></i><i></i></div><span class="badge"></span></div>
      <div class="foot-col news"><h4>LATEST NEWS</h4><ul><li>Effective Ethical Investment with Owen Marsh | Brindle Investment Insights Podcast</li><li>GDP Hotspots</li><li>Brindle Capital featured on Ledger Point Analytics' Webinar with Alan Reeve</li><li>Private sector capex: Not riding to the rescue</li></ul></div>
      <div class="foot-col register"><h4>REGISTER</h4><div class="reg-box"><p>Interested in investing with Brindle Capital?</p><span>Yes - I am ready to get started</span><span>Yes - I'm not ready to invest, but keep me updated on developments</span></div></div>
    </div>
    <div class="foot-legal"><p>The information on this site contains general information and does not take into account your personal objectives, financial situation or needs. Past performance is not an indication of future performance. Brindle Capital Management (ABN 12 345 678 901) is a Corporate Authorised Representative of Brindle Advice Pty Ltd - AFSL 402117. Click here for our Financial Services Guide.</p><p class="links">INVEST WITH US &nbsp; BLOG &nbsp; CLIENT LOGIN</p><p>Copyright 2019 © Brindle Capital</p></div>
  </footer>
</section>

<!-- Step 5: calculation -->
<section class="screen s5">
  <header class="site-head"><div class="brand"><span class="dot"></span>Brindle Capital</div><nav class="main-nav"><span class="current">INVEST WITH US ⌄</span><span>CONTENT ⌄</span><span>CLIENT LOGIN</span><span class="search"></span></nav></header>
  <main class="page">
    <div class="card">
      <div class="steps">
        <div class="step on"><span class="num">1</span><svg class="ico"><use href="#i-unit"/></svg><span class="lbl">PROPERTY TYPE</span></div>
        <div class="step on"><span class="num">2</span><svg class="ico"><use href="#i-pin"/></svg><span class="lbl">PROPERTY LOCATION</span></div>
        <div class="step on"><span class="num">3</span><svg class="ico"><use href="#i-value"/></svg><span class="lbl">PROPERTY VALUATION</span></div>
        <div class="step on"><span class="num">4</span><svg class="ico"><use href="#i-forecast"/></svg><span class="lbl">YOUR PROPERTY FORECAST</span></div>
        <div class="step on"><span class="num">5</span><svg class="ico"><use href="#i-calc"/></svg><span class="lbl">CALCULATION</span></div>
      </div>
      <div class="calc-form">
        <span class="cap" style="left:18px;top:14px">CHOOSE PROPERTY</span>
        <div class="select" style="left:18px;top:30px;width:209px">Sydney House</div>
        <span class="cap" style="left:253px;top:14px">CHOOSE ALTERNATIVE INVESTMENT</span>
        <div class="select" style="left:253px;top:30px;width:209px">Global Shares</div>
        <span class="cap" style="left:18px;top:75px">HOW MUCH WILL THE PROPERTY COST?</span>
        <div class="slider" style="left:19px;top:97px;width:170px"><span class="fill" style="width:90px"></span><span class="knob" style="left:90px"></span></div>
        <span class="slider-value" style="left:197px;top:93px">$500,000</span>
        <span class="cap" style="left:256px;top:76px">HOW MUCH WILL YOU INVEST?</span>
        <div class="slider" style="left:256px;top:98px;width:189px"><span class="fill" style="width:91px"></span><span class="knob" style="left:91px"></span></div>
        <span class="slider-value" style="left:454px;top:94px">$200,000</span>
      </div>
      <svg class="chart" width="515" height="486" viewBox="0 0 515 486" aria-label="Property versus shares line chart and yearly bar chart">
        <g stroke="#d6e3f2" stroke-width="1"><path d="M30 225H250M30 244H250M30 263H250M30 282H250M30 301H250"/></g>
        <path d="M30 225V320H250" fill="none" stroke="#333" stroke-width="1"/>
        <g text-anchor="end" style="font-size:5.5px"><text x="27" y="227">1000</text><text x="27" y="246">700</text><text x="27" y="265">500</text><text x="27" y="284">300</text><text x="27" y="303">100</text><text x="27" y="322">0</text></g>
        <g text-anchor="middle" style="font-size:5.5px"><text x="43" y="333">100</text><text x="63" y="333">200</text><text x="82" y="333">300</text><text x="102" y="333">400</text><text x="122" y="333">500</text><text x="141" y="333">600</text><text x="160" y="333">600</text><text x="180" y="333">700</text><text x="199" y="333">800</text><text x="218" y="333">900</text><text x="238" y="333">1000</text></g>
        <polyline points="43,280 60,280 82,244 101,300 122,263 144,263 158,300 178,300 198,280 218,298 244,280" fill="none" stroke="var(--teal)" stroke-width="1.4"/>
        <polyline points="43,298 60,311 82,280 101,300 122,280 158,280 178,242 198,300 218,300 244,225" fill="none" stroke="#1a3fe0" stroke-width="1.4"/>
        <g fill="#1a3fe0"><circle cx="43" cy="298" r="1.8"/><circle cx="60" cy="311" r="1.8"/><circle cx="82" cy="280" r="1.8"/><circle cx="101" cy="300" r="1.8"/><circle cx="122" cy="280" r="1.8"/><circle cx="158" cy="280" r="1.8"/><circle cx="178" cy="242" r="1.8"/><circle cx="198" cy="300" r="1.8"/><circle cx="218" cy="300" r="1.8"/><circle cx="244" cy="225" r="1.8"/></g>
        <g fill="var(--teal)"><circle cx="43" cy="280" r="1.8"/><circle cx="60" cy="280" r="1.8"/><circle cx="82" cy="244" r="1.8"/><circle cx="101" cy="300" r="1.8"/><circle cx="122" cy="263" r="1.8"/><circle cx="144" cy="263" r="1.8"/><circle cx="158" cy="300" r="1.8"/><circle cx="178" cy="300" r="1.8"/><circle cx="198" cy="280" r="1.8"/><circle cx="218" cy="298" r="1.8"/><circle cx="244" cy="280" r="1.8"/></g>

        <g style="font-size:5.5px" text-anchor="end"><text x="283" y="234">10K</text><text x="283" y="268">0K</text><text x="283" y="302">-20K</text></g>
        <path d="M286 224V326H484" fill="none" stroke="#333" stroke-width="1"/>
        <g fill="var(--teal-soft)"><rect x="287" y="244" width="196" height="9"/><rect x="287" y="261" width="196" height="9"/><rect x="287" y="278" width="196" height="9"/><rect x="287" y="295" width="196" height="9"/><rect x="287" y="311" width="196" height="9"/></g>
        <g fill="var(--teal)"><rect x="287" y="227" width="196" height="9"/><rect x="287" y="244" width="71" height="9"/><rect x="287" y="261" width="140" height="9"/><rect x="287" y="278" width="33" height="9"/><rect x="287" y="295" width="172" height="9"/><rect x="287" y="311" width="113" height="9"/></g>
        <g style="font-size:5px;fill:#777"><text x="361" y="251">40%</text><text x="430" y="268">70%</text><text x="323" y="285">20%</text><text x="462" y="302">80%</text><text x="403" y="318">60%</text></g>
        <g text-anchor="middle" style="font-size:5.5px"><text x="294" y="336">2019</text><text x="329" y="336">2021</text><text x="366" y="336">2023</text><text x="407" y="336">2024</text><text x="446" y="336">2025</text><text x="474" y="336">2026</text></g>
      </svg>
      <div class="results">
        <p class="result" style="left:16px;top:13px"><b>AFTER 5 YEARS</b>Shares will return $82,431 more</p>
        <p class="result" style="left:190px;top:13px"><b>AFTER 10 YEARS</b>Shares will return $160,176 more</p>
        <p class="result" style="left:373px;top:20px"><b>DEBT CONTRIBUTION</b></p>
      </div>
      <div class="btns" style="top:440px"><span class="btn prev">PREVIOUS</span><span class="btn next" style="min-width:76px">RECALCULATE</span></div>
    </div>
  </main>
  <footer class="site-foot">
    <div class="foot-main">
      <div class="foot-col about"><h4>ABOUT US</h4><p>Brindle Capital was formed to bridge the gap in investment solutions for everyday people looking for the middle ground between cookie-cutter robo-advice and high-cost financial planning.</p><p>Brindle Capital products put the power back in your hands:<br>⇒ tax efficient structures,<br>⇒ tailored to your ethics,<br>⇒ tailored to your risk,<br>⇒ tailored to your income needs,<br>⇒ fully transparent.</p><div class="social"><i></i><i></i><i></i><i></i><i></i><i></i><i></i></div><span class="badge"></span></div>
      <div class="foot-col news"><h4>LATEST NEWS</h4><ul><li>Effective Ethical Investment with Owen Marsh | Brindle Investment Insights Podcast</li><li>GDP Hotspots</li><li>Brindle Capital featured on Ledger Point Analytics' Webinar with Alan Reeve</li><li>Private sector capex: Not riding to the rescue</li></ul></div>
      <div class="foot-col register"><h4>REGISTER</h4><div class="reg-box"><p>Interested in investing with Brindle Capital?</p><span>Yes - I am ready to get started</span><span>Yes - I'm not ready to invest, but keep me updated on developments</span></div></div>
    </div>
    <div class="foot-legal"><p>The information on this site contains general information and does not take into account your personal objectives, financial situation or needs. Past performance is not an indication of future performance. Brindle Capital Management (ABN 12 345 678 901) is a Corporate Authorised Representative of Brindle Advice Pty Ltd - AFSL 402117. Click here for our Financial Services Guide.</p><p class="links">INVEST WITH US &nbsp; BLOG &nbsp; CLIENT LOGIN</p><p>Copyright 2019 © Brindle Capital</p></div>
  </footer>
</section>

</body>
</html>
```